Redesign website bus travel company Lenz Vals

We require a complete redesign of the website of Reisebüro Lenz Vals, an established bus tour operator based in Graubünden (www.lenzvals-beispiel.ch). For years, the company has specialized in multi-day tours throughout Europe, as well as day trips such as shopping trips to Innsbruck or Como, music tours, and market visits, primarily for seniors, as well as car rentals for clubs and companies.

The new website requires a video header with overlay text, red as the primary corporate color, complemented by black and gray, and a highly simplified navigation with two main sections: "Our Trips" and "Bus Rental." The remaining sections must be accessible via the "Menu" menu item. The design should be user-friendly for all age groups and mobile-responsive.

The goal is a trustworthy, modern website that reflects personal service and many years of experience.
The new logo can be found in the files, as well as a few pictures.

Target Market(s)

Guests of bus tours (day and multi-day trips) and bus rentals (clubs, companies, etc.)

Industry/Entity Type

Busreisen und Busvermietung

Number of Pages Required

1 page

Requirements
Must have
• Red as primary color, video header, simple UX for target group seniors
Nice to have
• Photo galleries of destinations and the vehicle fleet

```html
<!DOCTYPE html>
<html lang="de">
<head>
<meta charset="utf-8">
<title>Lenz Vals – Busreisen &amp; Busvermietung</title>
<link href="https://fonts.googleapis.com/css2?family=Playfair+Display:ital,wght@0,700;1,500;1,600;1,700&family=Poppins:wght@400;500;600&display=swap" rel="stylesheet">
<style>
:root{
  --red:#c4161c;
  --red-dark:#a50f14;
  --black:#111;
  --ink:#1d1d1d;
  --gray:#6b6b6b;
  --line:#dcdcdc;
  --navy:#0f1a33;
  --white:#fff;
  --gold:#f2b705;
}
*{box-sizing:border-box;margin:0;padding:0}
html,body{width:1200px;height:5386px;overflow:hidden}
body{font-family:"Poppins",sans-serif;color:var(--ink);background:#fff;position:relative}
.serif{font-family:"Playfair Display",serif;font-style:italic;font-weight:600}
.abs{position:absolute}
.btn{display:inline-flex;align-items:center;justify-content:center;background:var(--red);color:#fff;border-radius:6px;font-family:"Playfair Display",serif;font-style:italic;font-weight:600;font-size:15px;text-decoration:none}
section{position:absolute;left:0;width:1200px;overflow:hidden}

/* nav */
.nav{position:absolute;left:63px;top:0;width:1077px;height:75px;background:var(--red);border-radius:0 0 14px 14px;display:flex;align-items:center;padding:0 24px;z-index:5;box-shadow:0 4px 12px rgba(0,0,0,.25)}
.brand{color:#fff;font-family:"Poppins",sans-serif;font-weight:600;font-size:30px;letter-spacing:-.5px}
.nav-links{margin-left:auto;display:flex;gap:34px;color:#fff;font-size:15px;font-weight:500;margin-right:40px}
.burger{width:26px;display:flex;flex-direction:column;gap:5px}
.burger i{display:block;height:2px;background:#fff}

/* hero */
.hero{top:0;height:728px}
.hero-bg{position:absolute;inset:0;background:linear-gradient(180deg,#2e6fc0 0%,#5a8fd0 22%,#7aa54a 45%,#3f6a22 62%,#1b1b14 85%,#0a0a0a 100%)}
.hero h1{position:absolute;top:195px;width:100%;text-align:center;color:#fff;font-size:84px;font-weight:500}
.hero h2{position:absolute;top:300px;width:100%;text-align:center;color:#fff;font-size:38px;font-weight:500}
.hero .btn{position:absolute;left:509px;top:383px;width:182px;height:42px;font-family:"Poppins",sans-serif;font-style:normal;font-weight:500;font-size:16px}
.hero-note{position:absolute;left:836px;top:458px;width:210px;color:#fff;font-size:14px;line-height:1.6}
.play{position:absolute;left:562px;top:581px;width:76px;height:76px;border-radius:50%;background:#e9e9e9;display:flex;align-items:center;justify-content:center}

/* about */
.about{top:728px;height:777px;background:#fff}
.about h2{position:absolute;left:63px;top:90px;font-size:34px;line-height:1.35;color:var(--ink)}
.about .btn{position:absolute;left:972px;top:114px;width:168px;height:42px}
.tabs{position:absolute;left:58px;top:260px;width:576px;height:43px;border-radius:22px;background:#ececec;display:flex;align-items:center;padding:0 20px;font-size:18px}
.tabs span{padding:0 18px;border-right:1px solid #b9b9b9}
.tabs span:first-child{padding-left:0}
.tabs span:last-child{border:none;color:var(--red)}
.stat{position:absolute;top:390px;text-align:center}
.stat b{display:block;color:var(--red);font-family:"Playfair Display",serif;font-style:italic;font-weight:500;font-size:44px}
.stat em{display:block;font-family:"Playfair Display",serif;font-size:18px;line-height:1.15}
.about p{position:absolute;left:60px;top:562px;width:275px;font-size:15px;line-height:1.6}
.photo{position:absolute;border-radius:12px}

/* tours */
.tours{top:1505px;height:728px}
.dark-bg{position:absolute;inset:0;background:linear-gradient(180deg,#0c1730 0%,#1d3566 45%,#2c4f2a 80%,#1b2c14 100%)}
.sec-title{position:absolute;width:100%;text-align:center;font-size:34px;line-height:1.4}
.tours .sec-title,.rental .sec-title{color:#fff}
.filters{position:absolute;top:166px;left:0;width:100%;display:flex;justify-content:center;align-items:center;color:#fff;font-size:14px;gap:26px}
.filters .on{border:1.5px solid #fff;border-radius:8px;padding:4px 30px}
.filters .sep{opacity:.8}
.card{position:absolute;background:#fff;border-radius:8px;overflow:hidden}
.tour{top:240px;width:346px;height:439px}
.card .img{height:205px}
.tour h3{font-family:"Playfair Display",serif;font-style:italic;font-weight:600;font-size:18px;margin:18px 8px 10px}
.tour ul{margin:0 18px;font-size:14px;line-height:31px;list-style:none}
.tour li::before{content:"•";margin-right:10px}
.tour .btn{position:absolute;left:8px;bottom:16px;width:110px;height:40px}

/* experience */
.exp{top:2233px;height:830px;background:#fff}
.exp .sec-title{top:90px;color:var(--ink)}
.feat{position:absolute;left:63px;display:flex;gap:14px}
.feat svg{flex:none}
.feat h4{font-family:"Playfair Display",serif;font-style:italic;font-weight:600;font-size:16px;text-transform:uppercase;margin-top:2px}
.feat p{font-size:14px;line-height:1.65;color:var(--gray)}
.exp .btn{position:absolute;left:60px;top:701px;width:177px;height:40px;font-size:14px}

/* rental */
.rental{top:3063px;height:732px}
.rent{top:198px;width:346px;height:474px}
.rent .img{height:229px}
.rent h3{font-family:"Playfair Display",serif;font-weight:700;font-size:22px;margin:16px 16px 8px;letter-spacing:-.3px}
.rent p.d{font-size:11px;color:var(--gray);margin:0 16px;line-height:1.7;width:200px}
.price{margin:10px 16px;font-size:18px;font-weight:600}
.price small{font-size:11px;font-weight:400}
.specs{margin:0 16px;display:flex;gap:18px;font-size:9px;align-items:center}
.specs span{display:flex;align-items:center;gap:6px}
.specs i{display:inline-block;width:14px;height:10px;background:#222;border-radius:2px}
.rent .btn{position:absolute;left:16px;bottom:18px;width:110px;height:40px}

/* gallery */
.gallery{top:3795px;height:679px;background:#fff}
.gallery .sec-title{top:85px}
.slide{position:absolute;border-radius:10px;overflow:hidden;box-shadow:0 14px 30px rgba(0,0,0,.25)}
.slide span{position:absolute;left:0;right:0;bottom:18px;text-align:center;color:#fff;font-size:18px;font-weight:500}
.floor{position:absolute;left:180px;top:570px;width:840px;height:70px;border-radius:50%;background:radial-gradient(ellipse,rgba(0,0,0,.18),rgba(0,0,0,0) 70%)}

/* testimonials */
.reviews{top:4474px;height:575px;background:#fff}
.reviews .sec-title{top:44px}
.quote{position:absolute;width:343px;height:272px;border-radius:14px;background:#fff;border:2px solid #eee;box-shadow:0 6px 18px rgba(0,0,0,.06);text-align:center}
.quote.active{background:var(--red);color:#fff;border-color:var(--red)}
.quote h5{font-family:"Playfair Display",serif;font-weight:700;font-size:17px;margin-top:80px}
.quote p{font-size:14px;line-height:1.7;color:var(--gray);margin:14px 22px 0}
.quote.active p{color:#fff}
.quote .stars{position:absolute;bottom:24px;width:100%;color:var(--gold);font-size:16px;letter-spacing:4px}
.quote.active .stars{color:#fff}
.mark{position:absolute;font-family:"Playfair Display",serif;font-weight:700;font-size:64px;line-height:1}
.avatar{position:absolute;width:120px;height:100px;border-radius:10px;background:linear-gradient(160deg,#c9b9a6,#7a8da3)}
.arrow{position:absolute;top:4943px;width:32px;height:32px;border-radius:50%;display:flex;align-items:center;justify-content:center}

/* footer */
.footer{top:5049px;height:337px;background:var(--black);color:#fff}
.footer .brand-big{position:absolute;top:60px;width:100%;text-align:center;font-size:92px;font-weight:600;letter-spacing:-2px}
.footer .links{position:absolute;top:228px;width:100%;display:flex;justify-content:center;gap:40px;font-size:15px}
.footer hr{position:absolute;left:63px;top:281px;width:1077px;border:none;border-top:1px solid #555}
.footer .legal{position:absolute;left:63px;right:60px;top:303px;display:flex;font-size:11px;color:#bbb}
.footer .legal span.r{margin-left:auto;display:flex;gap:30px}
</style>
</head>
<body>

<section class="hero">
  <div class="hero-bg" role="img" aria-label="Reisebus von Lenz Vals auf einer Wiese unter blauem Himmel, Standbild des Header-Videos"></div>
  <nav class="nav">
    <div class="brand">Lenz Vals</div>
    <div class="nav-links"><span>Unsere Reisen</span><span>Busvermietung</span></div>
    <div class="burger"><i></i><i></i><i></i></div>
  </nav>
  <h1 class="serif">Komfortable</h1>
  <h2 class="serif">Europareisen &amp; Zuverlässige Busvermietung</h2>
  <a class="btn">Erfahren Sie Mehr</a>
  <svg class="abs" style="left:118px;top:462px" width="40" height="72" viewBox="0 0 40 72" fill="none" stroke="#fff" stroke-width="2"><circle cx="20" cy="18" r="16"/><line x1="20" y1="18" x2="20" y2="68"/><polyline points="10,58 20,68 30,58"/></svg>
  <p class="hero-note">Get your drone repaired quickly and professionally by our experienced team</p>
  <div class="play"><svg width="28" height="30" viewBox="0 0 28 30"><polygon points="4,2 26,15 4,28" fill="var(--red)"/></svg></div>
</section>

<section class="about">
  <h2 class="serif">Komfortable Touren. Persönlicher Service.<br>Erinnerungen, Die Bleiben</h2>
  <a class="btn">Erfahren Sie Mehr</a>
  <div class="tabs"><span>Unsere Geschichte</span><span>Unsere Mission</span><span>Unsere Vision</span></div>
  <div class="stat" style="left:68px"><b>20+</b><em>jahre<br>erfahrung</em></div>
  <div class="stat" style="left:198px"><b>99%</b><em>kundenz<br>friedenheit</em></div>
  <p>Empower your bu comprehensive agency solutions tai meetEmp your business with.</p>
  <div class="photo" style="left:334px;top:348px;width:349px;height:308px;background:linear-gradient(180deg,#8fb4d8 0%,#6c8a7a 40%,#5e9a3a 70%,#3f7a2a 100%)" role="img" aria-label="Musikanten in Tracht mit Alphorn vor dem Reisebus in den Bergen"></div>
  <div class="photo" style="left:702px;top:227px;width:438px;height:429px;background:linear-gradient(160deg,#9aa4ad 0%,#3c4148 50%,#1d1f23 100%)" role="img" aria-label="Zwei lächelnde Reisende vor dem Bus"></div>
</section>

<section class="tours">
  <div class="dark-bg" role="img" aria-label="Nächtliche Berglandschaft als Hintergrund"></div>
  <h2 class="sec-title serif" style="top:48px">Komfortable Busreisen Durch Europa Sorgfältig Geplant,<br>Mit Erfahrung Durchgeführt</h2>
  <div class="filters"><span class="on">Alle Reisen</span><span class="sep">|</span><span>Einmal</span><span class="sep">|</span><span>Mehrtägig</span><span class="sep">|</span><span>Saisonal</span><span class="sep">|</span><span>Musik</span><span class="sep">|</span><span>Einkaufen</span></div>
  <div class="card tour" style="left:63px">
    <div class="img" style="background:linear-gradient(180deg,#5d9be0 0%,#a6cde8 35%,#6aa43a 60%,#c2403a 85%,#5e8a2c 100%)" role="img" aria-label="Blumenwiese und Feldweg in der Toskana"></div>
    <h3>Frühlingsblumen In Der Toskana – 5 Tage</h3>
    <ul><li>20. Bis 24. April</li><li>Ab CHF 550</li><li>Geführte Tour + Hotel Inklusive</li></ul>
    <a class="btn">Buchung</a>
  </div>
  <div class="card tour" style="left:428px">
    <div class="img" style="background:linear-gradient(180deg,#6f8da8 0%,#b6c3cc 35%,#d8b07a 60%,#8a5a48 100%)" role="img" aria-label="Bunte Altstadthäuser in Innsbruck vor Bergkulisse"></div>
    <h3>Shopping In Innsbruck 1 Tag</h3>
    <ul><li>Jeden Samstag</li><li>CHF 49</li><li>Abfahrt: 8:00 Uhr Ab Chur</li></ul>
    <a class="btn">Buchung</a>
  </div>
  <div class="card tour" style="left:794px">
    <div class="img" style="background:linear-gradient(180deg,#5a86c4 0%,#8fb0d8 35%,#c48a5a 60%,#8a4a32 100%)" role="img" aria-label="Arena von Verona auf der Piazza"></div>
    <h3>Operntour Durch Verona &nbsp;3 Tage</h3>
    <ul><li>10. Bis 12. August</li><li>CHF 390</li><li>Inklusive Tickets + 3-Sterne Aufenthalt</li></ul>
    <a class="btn">Buchung</a>
  </div>
</section>

<section class="exp">
  <h2 class="sec-title serif">Jahrzehntelange Erfahrung. Persönlicher Service.<br>Reisen, Denen Sie Vertrauen Können</h2>
  <div class="feat" style="top:237px">
    <svg width="44" height="50" viewBox="0 0 44 50" fill="none" stroke="#222" stroke-width="2"><circle cx="22" cy="30" r="10"/><circle cx="22" cy="30" r="5"/><polygon points="22,2 24,7 29,7 25,10 27,15 22,12 17,15 19,10 15,7 20,7"/><polyline points="16,39 13,48 22,44 31,48 28,39"/></svg>
    <div><h4>Über 20 Jahre Erfahrung</h4><p>Lorem Ipsum Dolor Sit Amet Consecte<br>Proingravida Massa Nulla</p></div>
  </div>
  <div class="feat" style="top:358px">
    <svg width="44" height="50" viewBox="0 0 44 50" fill="none" stroke="#222" stroke-width="2"><path d="M4 36 V26 L10 18 H34 L40 26 V36 Z"/><circle cx="12" cy="38" r="4"/><circle cx="32" cy="38" r="4"/><line x1="4" y1="28" x2="40" y2="28"/><path d="M22 4 C14 4 14 14 22 16 C30 14 30 4 22 4Z"/></svg>
    <div><h4>Seniorenfreundliches Reisen</h4><p>Lorem Ipsum Dolor Sit Amet Consecte<br>Proingravida Massa Nulla</p></div>
  </div>
  <div class="feat" style="top:481px">
    <svg width="44" height="50" viewBox="0 0 44 50" fill="none" stroke="#222" stroke-width="2"><circle cx="22" cy="18" r="9"/><path d="M8 18 A14 14 0 0 1 36 18"/><rect x="5" y="16" width="5" height="9" rx="2"/><rect x="34" y="16" width="5" height="9" rx="2"/><path d="M6 48 C6 36 14 32 22 32 C30 32 38 36 38 48"/></svg>
    <div><h4>Persönlicher Service</h4><p>Lorem Ipsum Dolor Sit Amet Consecte<br>Proingravida Massa Nulla</p></div>
  </div>
  <div class="feat" style="top:602px">
    <svg width="44" height="50" viewBox="0 0 44 50" fill="none" stroke="#222" stroke-width="2"><circle cx="22" cy="14" r="9"/><path d="M12 12 H32"/><path d="M6 48 C6 34 14 28 22 28 C30 28 38 34 38 48"/><circle cx="22" cy="40" r="6"/></svg>
    <div><h4>Zuverlässige Fahrer</h4><p>Lorem Ipsum Dolor Sit Amet Consecte<br>Proingravida Massa Nulla</p></div>
  </div>
  <a class="btn">Entdecken Sie Mehr</a>
  <div class="abs" style="left:502px;top:244px;width:638px;height:470px;border-radius:40% 30% 20% 30%;background:radial-gradient(ellipse at 55% 50%,#4a9ad8 0%,#2a6fb0 45%,#e9eef3 72%,#fff 100%)" role="img" aria-label="Blauer Reisebus der Flotte in Seitenansicht"></div>
</section>

<section class="rental">
  <div class="dark-bg" style="background:linear-gradient(180deg,#13244a 0%,#2c4a78 40%,#3b5a3a 75%,#1d2b18 100%)" role="img" aria-label="Palmen und Abendhimmel als Hintergrund"></div>
  <h2 class="sec-title serif" style="top:62px">Zuverlässige Busvermietung Für Vereine,<br>Firmen Und Private Gruppen</h2>
  <div class="card rent" style="left:63px">
    <div class="img" style="background:linear-gradient(180deg,#9ec3e3 0%,#d7c3a3 45%,#a86a48 100%)" role="img" aria-label="Reisegruppe beim Ausblick über eine Schlucht"></div>
    <h3>Tagesmieten</h3>
    <p class="d">Our Drone Certifica Programs Are Designed Elevate Your</p>
    <p class="price">$120 <small>For 1 Day</small></p>
    <div class="specs"><span><i></i>10–20 Seats</span><span><i></i>Air Conditioning</span><span><i></i>Luxury Coaches</span></div>
    <a class="btn">Buchung</a>
  </div>
  <div class="card rent" style="left:428px">
    <div class="img" style="background:linear-gradient(180deg,#8fb6d8 0%,#b7c6b0 40%,#6f9a48 100%)" role="img" aria-label="Wandergruppe auf einem Bergpfad"></div>
    <h3>Mehrtägige Ausflüge</h3>
    <p class="d">Our Drone Certifica Programs Are Designed Elevate Your</p>
    <p class="price">$320 <small>Multi-Day Trips</small></p>
    <div class="specs"><span><i></i>10–20 Seats</span><span><i></i>Air Conditioning</span><span><i></i>Luxury Coaches</span></div>
    <a class="btn">Buchung</a>
  </div>
  <div class="card rent" style="left:794px">
    <div class="img" style="background:linear-gradient(180deg,#6f9fd6 0%,#c9d8e2 40%,#5c7a52 70%,#6d6d6d 100%)" role="img" aria-label="Bergstraße mit rotem Fahrzeug vor schneebedeckten Gipfeln"></div>
    <h3>Nationale oder internationale Reisen</h3>
    <p class="d">Our Drone Certifica Programs Are Designed Elevate Your</p>
    <p class="price">$620 <small>National Or International Trips</small></p>
    <div class="specs"><span><i></i>10–20 Seats</span><span><i></i>Air Conditioning</span><span><i></i>Luxury Coaches</span></div>
    <a class="btn">Buchung</a>
  </div>
</section>

<section class="gallery">
  <h2 class="sec-title serif">Momente Von Unterwegs – Sehen Sie, Wo Wir<br>Waren Und Mit Wem Wir Gereist Sind</h2>
  <div class="floor"></div>
  <div class="slide" style="left:0;top:310px;width:153px;height:169px;border-radius:0 10px 10px 0;background:linear-gradient(180deg,#c9cdb6,#5f6a3a);opacity:.85" role="img" aria-label="Hügellandschaft"></div>
  <div class="slide" style="left:167px;top:272px;width:255px;height:243px;background:linear-gradient(180deg,#d9c79c 0%,#8a8a4a 55%,#3d4a22 100%)" role="img" aria-label="Toskanische Hügel mit Zypressen"><span>Frühlingsblumen In Der</span></div>
  <div class="slide" style="left:435px;top:239px;width:332px;height:314px;background:linear-gradient(180deg,#4f86c6 0%,#9cc0de 40%,#4a7d9a 70%,#2f3a2a 100%)" role="img" aria-label="Reisegruppe vor dem Bus am Meer"><span>Frühlingsblumen In Der</span></div>
  <div class="slide" style="left:778px;top:272px;width:255px;height:243px;background:linear-gradient(180deg,#b99a8a 0%,#6d5a5a 55%,#2c2a2c 100%)" role="img" aria-label="Bus bei Sonnenuntergang"><span>Frühlingsblumen In Der</span></div>
  <div class="slide" style="left:1047px;top:310px;width:153px;height:169px;border-radius:10px 0 0 10px;background:linear-gradient(180deg,#c4cfc2,#5f6f4a);opacity:.85" role="img" aria-label="Landschaft im Frühling"><span style="text-align:left;left:24px">Frühlingsblume</span></div>
</section>

<section class="reviews">
  <h2 class="sec-title serif">Von Seeleuten Geschätzt, Durch Geschichten Bewiesen</h2>
</section>
<div class="quote" style="left:58px;top:4686px"><h5>Anna Keller</h5><p>Lorem ipsum dolor sit amet consectetur. Enim tristique neque amet amet. At morbi sodales dui elementum sed. Ac a mattis nisi facilisis volutpat.</p><div class="stars">★★★★★</div></div>
<div class="quote active" style="left:430px;top:4627px"><h5>Lea Brunner</h5><p>Lorem ipsum dolor sit amet consectetur. Enim tristique neque amet amet. At morbi sodales dui elementum sed. Ac a mattis nisi facilisis volutpat.</p><div class="stars">★★★★★</div></div>
<div class="quote" style="left:798px;top:4686px"><h5>Marco Caduff</h5><p>Lorem ipsum dolor sit amet consectetur. Enim tristique neque amet amet. At morbi sodales dui elementum sed. Ac a mattis nisi facilisis volutpat.</p><div class="stars">★★★★★</div></div>
<div class="avatar" style="left:170px;top:4648px" role="img" aria-label="Porträt der Kundin Anna Keller"></div>
<div class="avatar" style="left:541px;top:4590px;background:linear-gradient(160deg,#d8d8d8,#8f8f8f)" role="img" aria-label="Porträt der Kundin Lea Brunner"></div>
<div class="avatar" style="left:911px;top:4648px;background:linear-gradient(160deg,#9ec6de,#6a7a8a)" role="img" aria-label="Porträt des Kunden Marco Caduff"></div>
<div class="mark" style="left:342px;top:4740px;color:#111">”</div>
<div class="mark" style="left:78px;top:4884px;color:#111">“</div>
<div class="mark" style="left:712px;top:4680px;color:#fff">”</div>
<div class="mark" style="left:452px;top:4826px;color:#fff">“</div>
<div class="mark" style="left:1082px;top:4740px;color:#111">”</div>
<div class="mark" style="left:818px;top:4884px;color:#111">“</div>
<div class="arrow" style="left:552px;background:var(--red)"><svg width="14" height="14" viewBox="0 0 14 14" fill="none" stroke="#fff" stroke-width="2"><line x1="13" y1="7" x2="2" y2="7"/><polyline points="6,3 2,7 6,11"/></svg></div>
<div class="arrow" style="left:615px;border:1.5px solid var(--red)"><svg width="14" height="14" viewBox="0 0 14 14" fill="none" stroke="var(--red)" stroke-width="2"><line x1="1" y1="7" x2="12" y2="7"/><polyline points="8,3 12,7 8,11"/></svg></div>

<footer class="footer section" style="position:absolute;left:0;width:1200px">
  <div class="brand-big">Lenz Vals</div>
  <div class="links"><span>Unsere Reisen</span><span>Busvermietung</span></div>
  <hr>
  <div class="legal"><span>Copyright © 2025 All Right Reserved</span><span class="r"><span>Privacy Policy</span><span>Terms Of Service</span><span>Cookies Settings</span></span></div>
</footer>

</body>
</html>
```